Dozy Wren sleep comforter 'Local campaign' Billboard design

Billboard will be on display in a busy local street of Coburg. We want this to appeal to the fact that we are locals, we are mums, we care about mums, our factory is here, our staff are here and we support the community here. We like a possible support angle through the isolation of covid. For the purpose of design please refer to our:
Facebook: https://www.facebook.com/dozywrennaptoys
Insta: https://www.instagram.com/dozywren_naptoys
Or www.dozywrenhome.example

Designs look the same

```html
<!DOCTYPE html>
<html lang="en">
<head>
<meta charset="utf-8">
<title>Dozy Wren – Local Campaign Billboard</title>
<link href="https://fonts.googleapis.com/css2?family=Oswald:wght@300;500;600;700&family=Open+Sans:wght@400;700&display=swap" rel="stylesheet">
<style>
  :root {
    --ink: #0d0d0d;
    --paper: #ffffff;
    --gold: #c9a77a;
    --canvas: #e9e9e9;
    --text-dark: #2a2a2a;
    --photo-light: #f4f1ee;
    --photo-mid: #e6dcd6;
    --photo-skin: #d9b6a6;
  }
  * { margin: 0; padding: 0; box-sizing: border-box; }
  html, body { width: 800px; height: 1200px; overflow: hidden; }
  body {
    background: var(--canvas);
    position: relative;
    font-family: "Open Sans", Arial, sans-serif;
  }
  .billboard {
    position: absolute;
    left: 20px;
    top: 427px;
    width: 760px;
    height: 346px;
    background: var(--paper);
    box-shadow: 0 2px 6px rgba(0,0,0,0.15);
    overflow: hidden;
  }
  .billboard__main {
    position: absolute;
    left: 0; top: 0;
    width: 760px; height: 288px;
    background: var(--ink);
    overflow: hidden;
  }
  .billboard__art { position: absolute; left: 0; top: 0; }
  .billboard__message {
    position: absolute;
    left: 384px;
    top: 18px;
    width: 350px;
    color: var(--paper);
  }
  .brand {
    display: flex;
    align-items: center;
    gap: 7px;
    margin-bottom: 14px;
  }
  .brand__mark {
    width: 12px; height: 12px;
    background: var(--paper);
  }
  .brand__name {
    font-family: "Oswald", Arial, sans-serif;
    font-weight: 600;
    font-size: 17px;
    letter-spacing: 1px;
    color: var(--paper);
    line-height: 1;
  }
  .headline {
    font-family: "Oswald", Arial, sans-serif;
    text-transform: uppercase;
    line-height: 1.05;
  }
  .headline__intro { display: block; font-weight: 300; font-size: 30px; }
  .headline__care { display: block; font-weight: 600; font-size: 42px; }
  .headline__mums { display: block; font-weight: 700; font-size: 50px; color: var(--gold); }
  .rule {
    width: 34px; height: 3px;
    background: var(--gold);
    margin: 12px 0 10px;
  }
  .blurb {
    font-size: 10px;
    line-height: 1.45;
    width: 300px;
    color: var(--paper);
  }
  .billboard__contact {
    position: absolute;
    left: 0; top: 288px;
    width: 760px; height: 58px;
    display: flex;
    align-items: center;
    padding: 0 30px;
    color: var(--text-dark);
  }
  .contact__phone, .contact__web {
    display: flex; align-items: center; gap: 9px;
    font-family: "Oswald", Arial, sans-serif;
  }
  .contact__phone { font-weight: 500; font-size: 34px; letter-spacing: 0.5px; }
  .contact__web { margin-left: auto; font-weight: 600; font-size: 23px; }
</style>
</head>
<body>
  <section class="billboard">
    <div class="billboard__main">
      <svg class="billboard__art" width="760" height="288" viewBox="0 0 760 288">
        <defs>
          <radialGradient id="photoTone" cx="0.45" cy="0.5" r="0.6">
            <stop offset="0" stop-color="#d9b6a6"/>
            <stop offset="0.45" stop-color="#e6dcd6"/>
            <stop offset="1" stop-color="#f4f1ee"/>
          </radialGradient>
        </defs>
        <circle cx="130" cy="144" r="222" fill="#ffffff"/>
        <circle cx="130" cy="144" r="212" fill="none" stroke="#0d0d0d" stroke-width="5"/>
        <circle cx="130" cy="144" r="200" fill="url(#photoTone)" role="img" aria-label="Photo of a sleeping newborn wrapped in soft white knit, cradled in a mother's hands"/>
      </svg>

      <div class="billboard__message">
        <div class="brand">
          <span class="brand__mark"></span>
          <span class="brand__name">DOZY WREN</span>
        </div>
        <h1 class="headline">
          <span class="headline__intro">We are local</span>
          <span class="headline__care">We care about</span>
          <span class="headline__mums">Local mums</span>
        </h1>
        <div class="rule"></div>
        <p class="blurb">Comforters, formally known as ‘transitional objects’ are really important for many babies as they go through normal stages of development and start to foster independence.</p>
      </div>
    </div>

    <div class="billboard__contact">
      <div class="contact__phone">
        <svg width="26" height="26" viewBox="0 0 24 24" aria-hidden="true">
          <path fill="#c9a77a" d="M6.6 10.8a15.1 15.1 0 0 0 6.6 6.6l2.2-2.2c.3-.3.7-.4 1-.2 1.1.4 2.3.6 3.6.6.6 0 1 .4 1 1V20c0 .6-.4 1-1 1A17 17 0 0 1 3 4c0-.6.4-1 1-1h3.5c.6 0 1 .4 1 1 0 1.3.2 2.5.6 3.6.1.3 0 .7-.2 1z"/>
        </svg>
        <span>013.555.0148</span>
      </div>
      <div class="contact__web">
        <svg width="20" height="20" viewBox="0 0 24 24" aria-hidden="true" fill="none" stroke="#c9a77a" stroke-width="2">
          <circle cx="12" cy="12" r="10"/>
          <ellipse cx="12" cy="12" rx="4.5" ry="10"/>
          <line x1="2" y1="12" x2="22" y2="12"/>
        </svg>
        <span>www.dozywrenhome.example</span>
      </div>
    </div>
  </section>
</body>
</html>
```